looking for sleek business card to standout from the crowd!

We are a young biotechnology company looking to help you personalize your health through understanding your genetic make up. We need you help in making a clean but sleek business card design using our new logo. The goal? Any time we give our cards out, people say "nice card!" The feel we are going for is "modern-techy". We don't want to come across as an old, giant pharma company, but not trying to be a hipster either.

Target Market(s)

healthcare and biotechnology industry.

Industry/Entity Type

Biotechnology

Contact Information for Business Card

Info to include on the card will be NAME, TITLE, EMAIL, PHONE. The companies website (www.morvalytics.com) should also be on the card some where. Would like the logo, when printed, to be raised.

Requirements
Must have
• The logo we have attached in the color it is in. Fonts for text should lean toward more professional/tech.
Nice to have
• Prefer white/light color background
Should not have
• cartoons, landscape backgrounds images.

```html
<!DOCTYPE html>
<html lang="en">
<head>
<meta charset="utf-8">
<title>Morvalytics Business Card</title>
<link href="https://fonts.googleapis.com/css2?family=Montserrat:wght@400;600;700&display=swap" rel="stylesheet">
<style>
  :root {
    --bg: #e9ebee;
    --card: #ffffff;
    --blue: #1d76c0;
    --green: #84bd3e;
    --ink: #2e3440;
    --ink-light: #ffffff;
  }
  * { box-sizing: border-box; margin: 0; padding: 0; }
  html, body { width: 1200px; height: 857px; overflow: hidden; }
  body {
    background: var(--bg);
    font-family: "Montserrat", Arial, sans-serif;
    display: flex;
    align-items: center;
    justify-content: center;
    gap: 40px;
  }
  .card {
    position: relative;
    width: 540px;
    height: 309px;
    background: var(--card);
    overflow: hidden;
    box-shadow: 0 6px 18px rgba(0,0,0,0.12);
  }
  .card-bands { position: absolute; inset: 0; }
  .brand {
    position: absolute;
    color: var(--ink);
    font-weight: 600;
    font-size: 34px;
    letter-spacing: 2px;
    white-space: nowrap;
  }
  .card-back .brand { left: 50%; top: 50%; transform: translate(-50%, -50%); }
  .card-front .brand { left: 50%; top: 66px; transform: translateX(-50%); }
  .holder {
    position: absolute;
    right: 22px;
    top: 180px;
    text-align: right;
    color: var(--ink-light);
  }
  .holder-name { font-weight: 700; font-size: 17px; line-height: 1.1; }
  .holder-title { font-weight: 400; font-size: 9px; letter-spacing: 0.4px; margin-top: 2px; }
  .contact {
    position: absolute;
    left: 22px;
    top: 213px;
    color: var(--ink-light);
    font-size: 8.5px;
    line-height: 12px;
    font-weight: 600;
  }
  .contact-address { margin-bottom: 3px; }
  .contact-line { display: flex; align-items: center; gap: 6px; }
  .contact-line svg { width: 8px; height: 8px; flex: none; }
</style>
</head>
<body>

  <section class="card card-back" aria-label="Card back">
    <div class="brand">Morvalytics</div>
  </section>

  <section class="card card-front" aria-label="Card front">
    <svg class="card-bands" viewBox="0 0 540 309" width="540" height="309" aria-hidden="true">
      <polygon points="205,166 540,166 540,228 310,228" fill="var(--green)"/>
      <polygon points="0,200 178,200 245,238 540,238 540,309 0,309" fill="var(--blue)"/>
    </svg>

    <div class="brand">Morvalytics</div>

    <div class="holder">
      <div class="holder-name">Lina Marsh</div>
      <div class="holder-title">Graphic Designer</div>
    </div>

    <div class="contact">
      <div class="contact-address">
        Kenari RT 03 RW 02<br>
        Tamanasri Sidoarjo 61200<br>
        Jawa Timur
      </div>
      <div class="contact-line">
        <svg viewBox="0 0 8 8"><rect x="2" y="0.5" width="4" height="7" rx="0.8" fill="none" stroke="#fff" stroke-width="0.9"/></svg>
        <span>0856-XXXX-XXXX</span>
      </div>
      <div class="contact-line">
        <svg viewBox="0 0 8 8"><rect x="0.5" y="1.5" width="7" height="5" rx="0.6" fill="#fff"/><rect x="2" y="2.5" width="4" height="1.4" fill="var(--blue)"/></svg>
        <span>0856-XXXX-XXXX</span>
      </div>
      <div class="contact-line">
        <svg viewBox="0 0 8 8"><rect x="0.5" y="1.5" width="7" height="5" fill="#fff"/><polyline points="0.5,1.5 4,4.5 7.5,1.5" fill="none" stroke="var(--blue)" stroke-width="0.8"/></svg>
        <span>lina.marsh@mail.com</span>
      </div>
      <div class="contact-line">
        <svg viewBox="0 0 8 8"><circle cx="4" cy="4" r="3.4" fill="none" stroke="#fff" stroke-width="0.9"/><line x1="0.6" y1="4" x2="7.4" y2="4" stroke="#fff" stroke-width="0.7"/><ellipse cx="4" cy="4" rx="1.4" ry="3.4" fill="none" stroke="#fff" stroke-width="0.7"/></svg>
        <span>www.morvalytics.com</span>
      </div>
    </div>
  </section>

</body>
</html>
```